Brisley Global Sourcing - we are Asian sourcing agents

We are sourcing agents based in the USA and we act as sourcing agents for clients in throughout the world. We focus primarily on custom sewn goods. So basically companies who do not have the in-house expertise to do it themselves, come to us and have us find suitable factories in Asia to do the production. We are middlemen. We find the factories...quote the project...manage the quality control and then deliver the goods directly to our customer's door. We pride ourselves in making the communication very easy and precise.

Current page is www.brisleysourcing.com

I am not happy w/ the overall look. The spacing...the photos, the fonts...the design elements...the pictures. I want a cool, crisp design that conveys professionalism and clearly depicts/explains what we do.

Coding

Coded - Design and coding required

Number of Pages Required

5+ page

Requirements
Must have
• use my logo....I like it...it was designed by someone on this website.
Nice to have
• a video/animation of the entire process would be wonderful. Showing initial contact with our office in the USA...then to my correspondence with my offices in Taiwan and in Hong Kong...and then back and fort w/ the customer.....and then between my people in Hong Kong/Taiwan with the local factories......and then a quote is generated and sent to my client......to samples being made and sent for approval.....to a PO being generated......to final samples being sent.....to the order being shipped and delivered to the clients warehouse. I was thinking of an animation showing arrows and text showing the back and forth communication and explaining how the process flows.

```html
<!DOCTYPE html>
<html lang="en">
<head>
<meta charset="utf-8">
<title>Brisley Global Sourcing</title>
<link href="https://fonts.googleapis.com/css2?family=Source+Sans+3:wght@400;600;700&display=swap" rel="stylesheet">
<style>
:root{
  --navy:#12205c;
  --navy-dark:#0d1848;
  --green:#6f9a1c;
  --green-light:#8cb52b;
  --ink:#2b2b2b;
  --muted:#777;
  --line:#d8d8d8;
  --panel:#eeeeee;
  --footer:#333333;
  --white:#ffffff;
}
*{box-sizing:border-box;margin:0;padding:0}
html,body{width:1200px;height:2791px;overflow:hidden;background:var(--white)}
body{position:relative;font-family:"Source Sans 3",Arial,sans-serif;color:var(--ink)}
.abs{position:absolute}
.topbar{left:0;top:0;width:1200px;height:35px;background:var(--navy-dark)}
.topbar .account{position:absolute;right:96px;top:9px;color:var(--white);font-size:14px;font-weight:600}
.header{left:0;top:35px;width:1200px;height:108px}
.brand{position:absolute;left:100px;top:22px;display:flex;align-items:center;gap:14px}
.brand-dot{width:62px;height:62px;border-radius:50%;background:var(--navy)}
.brand-name{font-size:30px;font-weight:700;color:var(--navy);line-height:1}
.brand-sub{font-size:13px;color:var(--navy);letter-spacing:1px;margin-top:4px}
.search{position:absolute;left:614px;top:38px;width:466px;height:36px;border:2px solid var(--line);display:flex}
.search span{flex:1;padding:6px 0 0 40px;color:#aaa;font-size:16px;position:relative}
.search span svg{position:absolute;left:14px;top:9px}
.search b{width:88px;background:var(--green);color:var(--white);font-weight:400;font-size:17px;text-align:center;line-height:32px}
.nav{left:0;top:143px;width:1200px;height:50px;background:var(--navy)}
.nav ul{list-style:none;display:flex;position:absolute;left:92px;top:0;height:50px}
.nav li{color:var(--white);font-size:16px;padding:0 22px;line-height:50px;border-right:1px solid #2c3b78}
.nav li:last-child{border:none}
.social{position:absolute;right:96px;top:17px;display:flex;gap:9px}
.social i{width:16px;height:16px;border-radius:50%;background:var(--white);display:block}
.service{left:0;top:199px;width:1200px;height:45px;background:#e6e6e6;border-top:1px solid #d0d0d0;border-bottom:1px solid #d0d0d0}
.service div{position:absolute;top:12px;font-size:15px;color:var(--muted);display:flex;align-items:center;gap:10px}
.hero{left:100px;top:270px;width:996px;height:424px;background:linear-gradient(120deg,#c94a3e 0%,#d6cfc8 35%,#e7e2dc 60%,#b9c4c9 100%)}
.hero-text{position:absolute;right:22px;top:126px;text-align:left}
.hero-text span{display:block;background:var(--white);color:var(--green);font-size:60px;line-height:66px;padding:0 12px;border-radius:8px;margin-bottom:10px;width:max-content}
.quote-box{left:100px;top:722px;width:307px;height:249px;background:var(--navy);padding:18px 26px;color:var(--white)}
.quote-box h2{font-size:28px;font-weight:400}
.quote-box hr{width:62px;border:0;border-top:3px solid var(--green);margin:8px 0 10px}
.quote-box p{font-size:15px;line-height:20px}
.btn{display:inline-flex;align-items:center;gap:16px;color:var(--white);border-radius:12px;font-size:22px}
.quote-box .btn{position:absolute;left:30px;top:160px;width:246px;height:60px;background:linear-gradient(#8cb52b,#5d8a15);padding-left:26px}
.bags{left:424px;top:722px;width:673px;height:249px;background:#f0f0f0}
.bags .label{position:absolute;left:18px;top:36px;text-align:center;width:170px}
.bags .label small{font-size:13px;color:var(--ink)}
.bags .label strong{display:block;font-size:30px;letter-spacing:1px;margin:2px 0}
.bags p{position:absolute;left:16px;top:130px;width:180px;font-size:15px;line-height:20px;color:#555}
.bags .photo{position:absolute;left:200px;top:8px;width:460px;height:232px;background:linear-gradient(90deg,#3a3c44,#5d8fb9 40%,#b99060 65%,#e1916c 100%)}
.sec-title{font-size:30px;font-weight:400}
.sec-title+hr{border:0;border-top:1px solid var(--line);position:relative;margin-top:8px}
.sec-title+hr::before{content:"";position:absolute;left:0;top:-2px;width:64px;height:3px;background:var(--green)}
.main{left:100px;top:1016px;width:663px}
.body-text{font-size:16px;line-height:24px;margin-top:22px}
.tile{position:absolute;width:205px;height:252px;background:#f3f3f3}
.tile .pic{position:absolute;left:0;top:0;width:205px;height:200px}
.pic.bag{background:radial-gradient(ellipse 70px 50px at 50% 50%,#2f2f33 0%,#6b6b6e 50%,#f3f3f3 100%)}
.pic.cover{background:radial-gradient(ellipse 75px 55px at 50% 52%,#24357f 0%,#4f63b0 55%,#f3f3f3 100%)}
.pic.glove{background:radial-gradient(ellipse 65px 70px at 50% 48%,#222 0%,#c8c8c8 55%,#f3f3f3 100%)}
.pic.sport{background:radial-gradient(ellipse 60px 70px at 50% 50%,#b3232a 0%,#3a3a3a 55%,#f3f3f3 100%)}
.pic.case{background:linear-gradient(90deg,#f3f3f3 15%,#3a49b8 25%,#c23a9a 40%,#e0356a 55%,#7a3ab8 70%,#333 82%,#f3f3f3 90%)}
.pic.sewn{background:linear-gradient(135deg,#f3f3f3 12%,#d9d0c8 13%,#c96a5a 55%,#c81e2a 80%,#f3f3f3 81%)}
.tile .cap{position:absolute;left:0;bottom:0;width:205px;height:42px;background:var(--green);color:var(--white);font-size:22px;display:flex;align-items:center}
.tile .cap svg{margin:0 0 0 16px;flex:none}
.tile .cap span{flex:1;text-align:center;padding-right:30px;white-space:nowrap}
.tile .cap span.long{font-size:21px;padding-right:6px}
.sidebar{left:796px;top:1015px;width:301px;height:641px;background:#ececec;padding:18px 18px}
.sidebar h3{font-size:27px;font-weight:400;white-space:nowrap;letter-spacing:-.2px}
.sidebar hr{border:0;border-top:2px solid var(--green);width:80px;margin:6px 0 8px}
.sidebar ul{list-style:none}
.cat li{font-size:15px;color:var(--muted);height:35px;line-height:35px;border-bottom:1px solid #d5d5d5;padding-left:14px;position:relative}
.cat li::before{content:"»";position:absolute;left:0;color:#999}
.cat li.active{background:var(--white);border-left:3px solid var(--navy)}
.cat li.active::before{content:""}
.know li{font-size:15px;color:var(--muted);height:35px;line-height:35px;padding-left:20px;white-space:nowrap}
.cta{left:0;top:2143px;width:1200px;height:238px;background:linear-gradient(180deg,#f6f6f6,#ffffff 50%,#efefef)}
.cta .portrait{position:absolute;left:108px;top:39px;width:149px;height:158px;background:linear-gradient(#b35a4e,#6a6a70 60%,#2a2a30)}
.cta h2{position:absolute;left:294px;top:40px;font-size:30px;font-weight:400}
.cta p{position:absolute;left:294px;top:85px;font-size:17px}
.cta .btn{position:absolute;left:294px;top:130px;width:246px;height:60px;background:linear-gradient(#2a3d8a,#12205c);padding-left:26px}
.footer{left:0;top:2381px;width:1200px;height:357px;background:var(--footer);color:#ddd}
.footer h4{position:absolute;top:64px;font-size:12px;font-weight:700;color:var(--white)}
.info{position:absolute;left:100px;display:flex;gap:20px;font-size:12px;line-height:16px}
.info i{width:40px;height:40px;border-radius:50%;background:var(--navy);display:flex;align-items:center;justify-content:center;flex:none}
.widget{position:absolute;left:365px;top:98px;width:210px;height:190px;background:#3a3a3a;border-bottom:1px solid #666;font-size:12px}
.tags{position:absolute;left:628px;top:98px;width:230px;display:flex;flex-wrap:wrap;gap:8px}
.tags span{border:1px solid #888;font-size:9px;font-weight:700;padding:5px 7px;color:var(--white)}
.stores{position:absolute;left:891px;top:98px;width:210px;list-style:none}
.stores li{font-size:12px;font-weight:700;color:var(--white);height:37px;line-height:28px;border-bottom:1px solid #4a4a4a;display:flex;justify-content:space-between}
.stores li::after{content:"›";color:#888}
.copyright{left:0;top:2738px;width:1200px;height:53px;background:var(--green);color:var(--white);font-size:14px;text-align:center;line-height:53px}
</style>
</head>
<body>
<div class="abs topbar"><span class="account">Login | Register</span></div>

<header class="abs header">
  <div class="brand">
    <div class="brand-dot"></div>
    <div><div class="brand-name">BRISLEY</div><div class="brand-sub">GLOBAL SOURCING · USA · HONG KONG · TAIPEI</div></div>
  </div>
  <div class="search"><span><svg width="14" height="14" viewBox="0 0 14 14"><circle cx="6" cy="6" r="4.5" fill="none" stroke="#aaa" stroke-width="1.6"/><line x1="9.5" y1="9.5" x2="13" y2="13" stroke="#aaa" stroke-width="1.6"/></svg>Search</span><b>Search</b></div>
</header>

<nav class="abs nav">
  <ul><li>Home</li><li>Production</li><li>Categories</li><li>About Us</li><li>Request</li><li>Quote</li></ul>
  <div class="social"><i></i><i></i><i></i><i></i><i></i><i></i></div>
</nav>

<div class="abs service">
  <div style="left:115px"><svg width="22" height="16" viewBox="0 0 22 16"><rect x="1" y="1" width="16" height="11" fill="none" stroke="#888" stroke-width="1.5"/><rect x="5" y="4" width="16" height="11" fill="#e6e6e6" stroke="#888" stroke-width="1.5"/></svg>Customer service</div>
  <div style="left:330px"><svg width="18" height="16" viewBox="0 0 18 16"><path d="M8 1L1 7l7 6V9c4 0 7 1 9 5-1-5-4-8-9-8z" fill="#888"/></svg>3 Days Money Back Gaurantee</div>
  <div style="left:618px"><svg width="16" height="16" viewBox="0 0 16 16"><path d="M8 1l2 5h5l-4 3 2 5-5-3-5 3 2-5-4-3h5z" fill="#888"/></svg>5% Discount on order over $199</div>
</div>

<section class="abs hero" role="img" aria-label="Factory worker operating an industrial sewing machine with red fabric">
  <div class="hero-text"><span>Asian</span><span>Outsourcing</span><span>Made Easy!</span></div>
</section>

<aside class="abs quote-box">
  <h2>Request a Quote</h2><hr>
  <p>Please contact us for immediate consultation regarding your out-sourcing project.</p>
  <span class="btn">REQUEST QUOTE <svg width="30" height="22" viewBox="0 0 30 22"><path d="M0 7h16V0l14 11-14 11v-7H0z" fill="#fff"/></svg></span>
</aside>

<section class="abs bags">
  <div class="label"><small>— designer —</small><strong>HANDBAGS</strong><small>— collection —</small></div>
  <p>Mauris euismod lorem quis dolor pulvinar, vitae euismod sem posuere. Aliquam enim magna, faucibus.</p>
  <div class="photo" role="img" aria-label="Row of designer tote handbags in black, blue, olive and coral"></div>
</section>

<main class="abs main">
  <h2 class="sec-title">Sourcing&nbsp; custom goods in china</h2><hr>
  <p class="body-text">We outsource sewing services direct from China. Our long-established and extensive network of offshore factory-partners provides our clients with access to a wide variety of contract sewing expertise from Chinese manufacturers. Clients only need to communicate with our US agents, but will have the benefits of the cost savings &amp; quality workmanship from offshore outsourcing from Asia.</p>
</main>

<div class="tile" style="left:102px;top:1254px"><div class="pic bag" role="img" aria-label="Black and grey messenger bag"></div><div class="cap"><svg width="10" height="14" viewBox="0 0 10 14"><path d="M2 1l6 6-6 6" fill="none" stroke="#fff" stroke-width="2"/></svg><span>Bags</span></div></div>
<div class="tile" style="left:327px;top:1254px"><div class="pic cover" role="img" aria-label="Blue motorcycle cover"></div><div class="cap"><svg width="10" height="14" viewBox="0 0 10 14"><path d="M2 1l6 6-6 6" fill="none" stroke="#fff" stroke-width="2"/></svg><span>Covers</span></div></div>
<div class="tile" style="left:554px;top:1254px"><div class="pic glove" role="img" aria-label="Pair of black and white gloves"></div><div class="cap"><svg width="10" height="14" viewBox="0 0 10 14"><path d="M2 1l6 6-6 6" fill="none" stroke="#fff" stroke-width="2"/></svg><span>Gloves</span></div></div>
<div class="tile" style="left:102px;top:1549px"><div class="pic sport" role="img" aria-label="Red and black golf bag"></div><div class="cap"><svg width="10" height="14" viewBox="0 0 10 14"><path d="M2 1l6 6-6 6" fill="none" stroke="#fff" stroke-width="2"/></svg><span class="long">Sporting Goods</span></div></div>
<div class="tile" style="left:327px;top:1549px"><div class="pic case" role="img" aria-label="Row of colourful phone cases"></div><div class="cap"><svg width="10" height="14" viewBox="0 0 10 14"><path d="M2 1l6 6-6 6" fill="none" stroke="#fff" stroke-width="2"/></svg><span>Cases</span></div></div>
<div class="tile" style="left:554px;top:1549px"><div class="pic sewn" role="img" aria-label="Hands sewing red fabric on a machine"></div><div class="cap"><svg width="10" height="14" viewBox="0 0 10 14"><path d="M2 1l6 6-6 6" fill="none" stroke="#fff" stroke-width="2"/></svg><span>Sewn Goods</span></div></div>

<aside class="abs sidebar">
  <h3>Sourcing&nbsp; Solutions</h3><hr>
  <ul class="cat"><li>Bags</li><li class="active">Cases</li><li>Covers</li><li>Gloves</li><li>Medical</li><li>Sewn Goods</li><li>Sporting Goods</li></ul>
  <h3 style="margin-top:26px">What you ned to know</h3><hr>
  <ul class="know"><li>Contract Sewing in China</li><li>What is the Process?</li><li>What the Minimum Order?</li><li>Contract Outsourcing FAQ</li><li>Outsourcing Case Study</li><li>Custom Industrial Sewing in China</li></ul>
</aside>

<section class="abs" style="left:100px;top:1842px;width:663px">
  <h2 class="sec-title">Don't go it alone</h2><hr>
  <p class="body-text" style="margin-top:18px">Brisley Global Sourcing has been sourcing custom sewn goods in Asia since 1998. We work with our clients by matching their unique production needs with the best possible China sewing factories. We manage the entire process from start to finish, by first identify-ing the best factories to quote each job. The next step is negotiating the best (fair) price possible. We complete the process by monitoring the quality of the goods during produc-tion, and then managing the ocean logistics, customs clearances and local delivery right to your door. Our services and our total commitment to customer satisfaction help level the playing field by giving our customers&nbsp; to low cost, high quality China contract sewing.</p>
</section>

<section class="abs cta">
  <div class="portrait" role="img" aria-label="Portrait of the company founder"></div>
  <h2>Outsource Your Sewing Needs to Trusted Contractors in China</h2>
  <p>Please contact us for immediate consultation regarding your outsourcing project.</p>
  <span class="btn">REQUEST QUOTE <svg width="30" height="22" viewBox="0 0 30 22"><path d="M0 7h16V0l14 11-14 11v-7H0z" fill="#fff"/></svg></span>
</section>

<footer class="abs footer">
  <h4 style="left:100px">ABOUT US</h4>
  <h4 style="left:365px">FRIENDBOOK LIKE US</h4>
  <h4 style="left:628px">PRODUCT TAGS</h4>
  <h4 style="left:891px">OUR STORES</h4>
  <div class="info" style="top:100px"><i><svg width="18" height="18" viewBox="0 0 18 18"><path d="M4 1l3 4-2 2c1 2 3 4 5 5l2-2 4 3-2 3C8 16 2 10 1 4z" fill="#fff"/></svg></i><div>Our support hotline is available<br>24/5 a day: +44.5550001234,<br>+1.5550004321</div></div>
  <div class="info" style="top:164px"><i><svg width="18" height="18" viewBox="0 0 18 18"><circle cx="9" cy="10" r="7" fill="none" stroke="#fff" stroke-width="2"/><path d="M9 6v4h3" stroke="#fff" stroke-width="2" fill="none"/></svg></i><div>Mo – Fr 9.00 – 17.00<br>Sa 9.00 – 15.00<br>Su Closed</div></div>
  <div class="info" style="top:228px"><i><svg width="18" height="18" viewBox="0 0 18 18"><rect x="2" y="3" width="14" height="12" fill="none" stroke="#fff" stroke-width="2"/><path d="M9 5v7M6 9l3 3 3-3" stroke="#fff" stroke-width="1.6" fill="none"/></svg></i><div><b>Delivery</b><br>USA / Europe / Worldwide</div></div>
  <div class="widget">
    <div style="padding:8px 14px;color:#fff;font-weight:700">northpeak-themes.com</div>
    <div style="padding:2px 14px;color:#aaa;font-size:10px">12 people like northpeak-themes.com</div>
    <div style="position:absolute;left:10px;top:60px;width:200px;height:100px;background:linear-gradient(90deg,#6b7c8a,#8a7a6e,#5a5a5a)" role="img" aria-label="Grid of follower profile thumbnails"></div>
    <div style="position:absolute;left:10px;top:170px;color:#aaa;font-size:10px">Friendbook social plugin</div>
  </div>
  <div class="tags"><span>ACCESSORIES</span><span>BIKINI</span><span>FISHING EQUIPMENT</span><span>LURE</span><span>REEL</span><span>ROD</span><span>SWIMGEAR</span><span>SWIMMING</span><span>SWIMWEAR</span></div>
  <ul class="stores"><li>London</li><li>Dubai</li><li>Berlin</li><li>New York</li><li>Moscow</li></ul>
</footer>

<div class="abs copyright">Copyright © 2015 Brisley Global Sourcing, LLC. | USA - Hong Kong - Taipei</div>
</body>
</html>
```